Insurance company needs a business card design

We need a business card design for a Massachusetts-based insurance company Veloria Insurance, LLC. We provide auto insurance to Hispanic (Spanish- or Portuguese-speaking) immigrants in the United States. We will give these business cards to auto dealers where such customers typically go to purchase vehicles. We will provide a solution to the dealers to provide easy insurance to the customers buying cars at their dealerships. Veloria is the Spanish word for protection.
Contact Information for Business Card
Name, Designation, Company Name, Address, Phone Number, Email, Website
Look and feel
Each slider illustrates characteristics of the customer's brand and the style your logo design should communicate.

```html
<!DOCTYPE html>
<html lang="en">
<head>
<meta charset="utf-8">
<title>Veloria Insurance – Business Card</title>
<link href="https://fonts.googleapis.com/css2?family=Montserrat:wght@700;800&family=Open+Sans:wght@400;600&display=swap" rel="stylesheet">
<style>
  :root {
    --navy: #0a4a7c;
    --orange: #f0831f;
    --ink: #1d1d1d;
    --paper: #ffffff;
    --stage: #2b2b2d;
  }
  * { box-sizing: border-box; margin: 0; padding: 0; }
  html, body { width: 1200px; height: 900px; overflow: hidden; }
  body {
    background: var(--stage);
    font-family: "Open Sans", Arial, sans-serif;
    display: flex; flex-direction: column; align-items: center; justify-content: center; gap: 48px;
  }
  .card {
    width: 660px; height: 377px; border-radius: 22px; position: relative; overflow: hidden;
  }
  /* Front */
  .card-front { background: var(--paper); color: var(--ink); }
  .brand {
    position: absolute; left: 120px; top: 62px;
    display: flex; align-items: center; gap: 14px;
  }
  .brand-mark { width: 30px; height: 30px; background: var(--orange); }
  .brand-name {
    font-family: "Montserrat", Arial, sans-serif; font-weight: 800;
    color: var(--navy); font-size: 34px; letter-spacing: 1px; line-height: 1;
  }
  .divider {
    position: absolute; left: 48px; right: 48px; top: 196px; height: 1px; background: var(--ink);
  }
  .contacts { position: absolute; left: 48px; top: 212px; list-style: none; font-size: 14px; line-height: 22px; }
  .contacts li { display: flex; align-items: center; gap: 8px; }
  .contacts svg { width: 12px; height: 12px; fill: var(--orange); flex: none; }
  .person { position: absolute; right: 48px; top: 124px; text-align: right; }
  .person-name {
    font-family: "Montserrat", Arial, sans-serif; font-weight: 800; font-size: 26px; letter-spacing: 1px;
  }
  .person-name .first { color: var(--navy); }
  .person-name .last { color: var(--orange); }
  .person-title { font-size: 15px; margin-top: 2px; }
  .address { position: absolute; right: 48px; top: 212px; text-align: right; font-size: 14px; line-height: 22px; }
  .edge-band { position: absolute; left: 0; right: 0; bottom: 0; height: 12px; display: flex; }
  .edge-band .navy { width: 34%; background: var(--navy); clip-path: polygon(0 0, 100% 0, 96% 100%, 0 100%); }
  .edge-band .orange { flex: 1; background: var(--orange); margin-left: -6px; clip-path: polygon(2% 0, 100% 0, 100% 100%, 0 100%); }
  /* Back */
  .card-back {
    background: var(--navy); display: flex; align-items: center; justify-content: center; gap: 18px;
  }
  .card-back .brand-mark { width: 40px; height: 40px; }
  .card-back .brand-name { color: var(--paper); font-size: 52px; }
</style>
</head>
<body>
  <section class="card card-front" aria-label="Card front">
    <div class="brand">
      <span class="brand-mark"></span>
      <span class="brand-name">VELORIA INSURANCE</span>
    </div>
    <div class="person">
      <p class="person-name"><span class="first">MARCO</span> <span class="last">DELANEY</span></p>
      <p class="person-title">Founder</p>
    </div>
    <div class="divider"></div>
    <ul class="contacts">
      <li><svg viewBox="0 0 12 12"><rect x="3" y="0" width="6" height="12" rx="1.5"/></svg>(555) 014-2290</li>
      <li><svg viewBox="0 0 12 12"><path d="M1 4c0-2 10-2 10 0v1H8V3.5H4V5H1z"/><rect x="2" y="6" width="8" height="5" rx="1"/></svg>(555) 014-2290</li>
      <li><svg viewBox="0 0 12 12"><path d="M0 2h12v8H0z M0 2l6 5 6-5" stroke="#fff" stroke-width="1"/></svg>info@veloriainsurance.com</li>
      <li><svg viewBox="0 0 12 12"><circle cx="6" cy="6" r="6"/></svg>www.veloriainsurance.com</li>
    </ul>
    <address class="address" style="font-style:normal">
      2185 Harlow Street<br>Springfield, MA 01103
    </address>
    <div class="edge-band"><span class="navy"></span><span class="orange"></span></div>
  </section>

  <section class="card card-back" aria-label="Card back">
    <span class="brand-mark"></span>
    <span class="brand-name">VELORIA INSURANCE</span>
  </section>
</body>
</html>
```